Verdant Medispa Business Card

need a business card for our medispa, attached please see the logo.
our website is https://verdantmedispa-example.com

Sorina Belcourt, MD
Internal Medicine

555-204-7193

Sorina@verdantmedispa-example.com

Www.Verdantmedispa-example.com

738 E Harlow Blvd N, Ste 512, Katy, TX 77981

Target Market(s)

MedSpa, Cosmetics, Esthetics

Industry/Entity Type

MedicalSpa

Contact Information for Business Card

Please see the attached business card which i pulled from the internet. I like the idea back as a logo and front with info.

Font styles to use
Decorative

Requirements
Must have
• Color should be matching with Logo and Website theme, Also I like to have QR code for the website

```html
<!DOCTYPE html>
<html lang="en">
<head>
<meta charset="utf-8">
<title>Verdant Medispa Business Card</title>
<link href="https://fonts.googleapis.com/css2?family=Montserrat:wght@500;700&family=Open+Sans:wght@400&display=swap" rel="stylesheet">
<style>
  :root {
    --page-bg: #ece8e3;
    --card-bg: #7d6653;
    --card-bg-light: #8a7360;
    --gold: #e3c130;
    --gold-edge: #c9a520;
  }
  * { margin: 0; padding: 0; box-sizing: border-box; }
  html, body {
    width: 1200px; height: 913px; overflow: hidden;
    background: var(--page-bg);
  }
  .canvas {
    position: relative; width: 1200px; height: 913px;
    display: flex; flex-direction: column; align-items: center;
    justify-content: center; gap: 36px;
  }
  .card {
    position: relative; width: 700px; height: 400px;
    border-radius: 30px;
    background: linear-gradient(135deg, var(--card-bg) 0%, var(--card-bg-light) 55%, var(--card-bg) 100%);
    border: 2px solid var(--gold-edge);
    color: var(--gold);
    box-shadow: 0 8px 22px rgba(40, 30, 20, 0.25);
  }
  .card-front { display: flex; align-items: center; justify-content: center; }
  .brand { display: flex; align-items: center; gap: 16px; }
  .brand-dot { width: 22px; height: 22px; border-radius: 50%; background: var(--gold); }
  .brand-name {
    font-family: "Montserrat", sans-serif; font-weight: 500;
    font-size: 50px; letter-spacing: 1px; color: var(--gold);
  }
  .card-back { display: flex; align-items: center; padding-left: 20px; }
  .identity {
    width: 330px; text-align: right; padding-right: 22px;
    font-family: "Montserrat", sans-serif; white-space: nowrap;
  }
  .identity-name { font-weight: 700; font-size: 22px; letter-spacing: 0.3px; }
  .identity-title {
    font-family: "Open Sans", sans-serif; font-weight: 400;
    font-size: 19px; margin-top: 2px;
  }
  .divider { width: 1.5px; height: 150px; background: var(--gold); flex: none; }
  .contacts {
    list-style: none; padding-left: 20px; white-space: nowrap;
    font-family: "Open Sans", sans-serif; font-size: 15px; line-height: 1.45;
  }
  .contacts li { display: flex; align-items: flex-start; gap: 9px; margin: 3px 0; }
  .contacts svg { width: 14px; height: 14px; flex: none; margin-top: 3px; fill: var(--gold); }
  .website-qr {
    position: absolute; right: 28px; bottom: 26px;
    width: 64px; height: 64px;
    border: 2px solid var(--gold); border-radius: 4px;
  }
</style>
</head>
<body>
<main class="canvas">
  <section class="card card-front" aria-label="Card front">
    <div class="brand">
      <span class="brand-dot"></span>
      <span class="brand-name">Verdant Medispa</span>
    </div>
  </section>

  <section class="card card-back" aria-label="Card back">
    <div class="identity">
      <p class="identity-name">SORINA BELCOURT, MD</p>
      <p class="identity-title">Internal Medicine</p>
    </div>
    <div class="divider"></div>
    <ul class="contacts">
      <li>
        <svg viewBox="0 0 16 16" aria-hidden="true"><path d="M8 0a5.5 5.5 0 0 0-5.5 5.5C2.5 9.6 8 16 8 16s5.5-6.4 5.5-10.5A5.5 5.5 0 0 0 8 0zm0 8a2.5 2.5 0 1 1 0-5 2.5 2.5 0 0 1 0 5z"/></svg>
        <span>738 E Harlow Blvd N<br>Ste 512, Katy, TX 77981</span>
      </li>
      <li>
        <svg viewBox="0 0 16 16" aria-hidden="true"><path d="M3.6 1.2 6 3.6c.4.4.4 1 0 1.4L4.8 6.2a9 9 0 0 0 5 5L11 10c.4-.4 1-.4 1.4 0l2.4 2.4c.4.4.4 1 0 1.4l-1.3 1.3c-.8.8-2 1-3 .5A17 17 0 0 1 .4 5.5c-.5-1-.3-2.2.5-3L2.2 1.2c.4-.4 1-.4 1.4 0z"/></svg>
        <span>555-204-7193</span>
      </li>
      <li>
        <svg viewBox="0 0 16 16" aria-hidden="true"><path d="M1 3h14v1.2L8 9 1 4.2V3zm0 2.6 7 4.8 7-4.8V13H1V5.6z"/></svg>
        <span>Sorina@verdantmedispa-example.com</span>
      </li>
      <li>
        <svg viewBox="0 0 16 16" aria-hidden="true"><path d="M8 0a8 8 0 1 0 0 16A8 8 0 0 0 8 0zm5.9 7h-2.6a12 12 0 0 0-1-4.8A6 6 0 0 1 13.9 7zM8 2c.7.9 1.2 2.7 1.3 5H6.7C6.8 4.7 7.3 2.9 8 2zM5.7 2.2a12 12 0 0 0-1 4.8H2.1a6 6 0 0 1 3.6-4.8zM2.1 9h2.6a12 12 0 0 0 1 4.8A6 6 0 0 1 2.1 9zM8 14c-.7-.9-1.2-2.7-1.3-5h2.6c-.1 2.3-.6 4.1-1.3 5zm2.3-.2a12 12 0 0 0 1-4.8h2.6a6 6 0 0 1-3.6 4.8z"/></svg>
        <span>www.Verdantmedispa-example.com</span>
      </li>
    </ul>
    <div class="website-qr" role="img" aria-label="Space for the website QR code"></div>
  </section>
</main>
</body>
</html>
```